New Zealand health product business needs website designed

A website is required for a business that sells New Zealand made products, namely products like infant formula, health products such as NZ honey, supplements, skincare products etc. This is purely an informative website that will introduce the all the different types of products the business has to offer. The target audience will the the Chinese market. The logo is a calligraphy style font in colours 78b643 and 313542 (logo is still being finalised at the moment) so a colour theme to match would be great.

It is crucial that the design communicates the beautiful nature of New Zealand, non-polluted environments, with emphasis on pure, natural and cleaniness.
Updates

A website that I quite like is http://www.frostvalegelato.co.nz

Information is easy to find, layout is nice and clear.                          

Hi all, I have now uploaded a logo for the business "Tawny Crate", please note that this is yet to be finalized however I expect it to be minor changes so please ensure the website theme and colour use go well with the logo. 

There are three scenery images uploaded, designs with any one of them used is fine whichever works better with your design.  Only one image is required on the website, no sliding effects for this.

Also just to clarify my requirements further.  The developer can use HTML, PHP, Javascript, CSS for coding, preferably to have the images cut and a pdf guide provided for things like alignment and sizing etc.

The menu items are Home / Our story / Product outline / Brands / Contact us
Designs are required for all these.  Within the product outline page, the subcategories are -
Infant formulas
Baby supplements
Toddlers products
Honey
Beauty products
Mens supplements
Womens supplements
Health products
Others

   

Target Market(s)

China based customers looking for quality products from New Zealand.

Industry/Entity Type

Health

Requirements
Must have
• clear menu bar in home page, the four main menu items are -
Our story
Product outline
Brands
Contact us
Nice to have
• Space for a large scenery photo in the home page

```html
<!DOCTYPE html>
<html lang="en">
<head>
<meta charset="utf-8">
<title>Tawny Crate – Quality Products from New Zealand</title>
<link rel="stylesheet" href="https://fonts.googleapis.com/css2?family=Arimo:wght@400;700&family=Kaushan+Script&display=swap">
<style>
  :root {
    --outer: #000000;
    --header-bg: #313542;
    --page-bg: #252836;
    --nav-bg: #000000;
    --nav-text: #b4b6bc;
    --nav-divider: #c9cbd1;
    --rule: #8d8f99;
    --brand-green: #78b643;
    --subline: #8a8d97;
    --headline: #313542;
    --tagline: #4f5566;
    --card-bg: #1e2029;
    --card-text: #a9abb3;
    --card-rule: #7d84a8;
    --font-text: "Arimo", Arial, sans-serif;
    --font-display: "Kaushan Script", cursive;
  }
  * { box-sizing: border-box; margin: 0; padding: 0; }
  html, body {
    width: 1200px;
    height: 1029px;
    overflow: hidden;
    background: var(--outer);
    font-family: var(--font-text);
  }
  .page {
    position: absolute;
    left: 113px;
    top: 0;
    width: 972px;
    height: 1029px;
    background: var(--page-bg);
  }
  .site-header {
    position: relative;
    height: 185px;
    background: var(--header-bg);
    border-bottom: 2px solid var(--rule);
  }
  .brand {
    position: absolute;
    left: 118px;
    top: 72px;
    display: flex;
    align-items: baseline;
    gap: 14px;
  }
  .brand-name {
    color: var(--brand-green);
    font-weight: 700;
    font-size: 52px;
    letter-spacing: -0.5px;
  }
  .brand-subline {
    color: var(--subline);
    font-size: 18px;
  }
  .main-nav {
    height: 43px;
    background: var(--nav-bg);
    position: relative;
  }
  .main-nav ul {
    list-style: none;
    position: absolute;
    left: 68px;
    top: 8px;
    display: flex;
    border-left: 2px solid var(--nav-divider);
  }
  .main-nav li {
    width: 210px;
    height: 25px;
    border-right: 2px solid var(--nav-divider);
    text-align: center;
    line-height: 25px;
    color: var(--nav-text);
    font-size: 16.5px;
  }
  .hero {
    position: relative;
    height: 455px;
    border-bottom: 2px solid var(--rule);
  }
  .hero-photo {
    position: absolute;
    inset: 0;
    background: linear-gradient(180deg, #8a8e99 0%, #b9bcc5 22%, #c9ccd4 40%, #8f95a2 60%, #5d6470 78%, #6a5f48 88%, #817868 94%, #9a9da4 100%);
  }
  .hero-title {
    position: absolute;
    left: 80px;
    top: 40px;
    font-family: var(--font-display);
    font-size: 47px;
    color: var(--headline);
    letter-spacing: 2px;
    font-weight: 400;
  }
  .hero-tagline {
    position: absolute;
    left: 84px;
    top: 107px;
    font-size: 20px;
    color: var(--tagline);
  }
  .topics {
    position: absolute;
    left: 66px;
    top: 725px;
    display: flex;
    border-left: 2px solid var(--card-rule);
  }
  .topic {
    width: 210px;
    height: 159px;
    padding-left: 10px;
    border-right: 2px solid var(--card-rule);
  }
  .topic-card {
    width: 189px;
    height: 159px;
    background: var(--card-bg);
  }
  .topic-photo { height: 85px; }
  .topic-photo.rocks { background: linear-gradient(180deg, #3aa39a 0%, #b8955e 35%, #a27a4c 70%, #4c9b8e 100%); }
  .topic-photo.stream { background: linear-gradient(135deg, #6b5a4f 0%, #a58a78 40%, #c9c4bc 70%, #7f7265 100%); }
  .topic-photo.pebbles { background: linear-gradient(135deg, #2f6b66 0%, #3e8a82 45%, #8c7d7a 60%, #356f6b 100%); }
  .topic-photo.water { background: linear-gradient(160deg, #4a4039 0%, #a9a4a0 40%, #5a4f47 65%, #c6c3c2 100%); }
  .topic-title {
    margin: 12px 0 0 8px;
    color: var(--brand-green);
    font-weight: 700;
    font-size: 14px;
  }
  .topic-text {
    margin: 2px 0 0 8px;
    color: var(--card-text);
    font-size: 14px;
    line-height: 17px;
  }
  .social {
    position: absolute;
    left: 155px;
    top: 959px;
    display: flex;
    gap: 11px;
    list-style: none;
  }
  .social li {
    width: 27px;
    height: 27px;
    border-radius: 3px;
  }
  .social .net-one { background: #3b5998; }
  .social .net-two { background: #e4e6e8; }
  .social .net-three { background: #c4302b; }
</style>
</head>
<body>
  <div class="page">
    <header class="site-header">
      <div class="brand">
        <span class="brand-name">Tawny Crate</span>
        <span class="brand-subline">Subline logo this is the subline</span>
      </div>
    </header>

    <nav class="main-nav">
      <ul>
        <li>Our story</li>
        <li>Product outline</li>
        <li>Brands</li>
        <li>Contact us</li>
      </ul>
    </nav>

    <section class="hero">
      <div class="hero-photo" role="img" aria-label="New Zealand fiord landscape with misty mountains, cloudy sky, a lone tree and calm water"></div>
      <h1 class="hero-title">Clear air. Clean water. Pure nature.</h1>
      <p class="hero-tagline">Quality Products from New Zealand</p>
    </section>

    <section class="topics">
      <article class="topic">
        <div class="topic-card">
          <div class="topic-photo rocks" role="img" aria-label="Sandstone rocks by turquoise sea"></div>
          <h2 class="topic-title">Topic 1</h2>
          <p class="topic-text">Lorem ipsum dolor sit amet, consectetuer adipiscing...</p>
        </div>
      </article>
      <article class="topic">
        <div class="topic-card">
          <div class="topic-photo stream" role="img" aria-label="Pebbles under clear stream water"></div>
          <h2 class="topic-title">Topic 2</h2>
          <p class="topic-text">Lorem ipsum dolor sit amet, consectetuer adipiscing...</p>
        </div>
      </article>
      <article class="topic">
        <div class="topic-card">
          <div class="topic-photo pebbles" role="img" aria-label="Green river stones in water"></div>
          <h2 class="topic-title">Topic 3</h2>
          <p class="topic-text">Lorem ipsum dolor sit amet, consectetuer adipiscing...</p>
        </div>
      </article>
      <article class="topic">
        <div class="topic-card">
          <div class="topic-photo water" role="img" aria-label="Close-up of rippling water surface"></div>
          <h2 class="topic-title">Topic 4</h2>
          <p class="topic-text">Lorem ipsum dolor sit amet, consectetuer adipiscing...</p>
        </div>
      </article>
    </section>

    <ul class="social" aria-label="Social links">
      <li class="net-one"></li>
      <li class="net-two"></li>
      <li class="net-three"></li>
    </ul>
  </div>
</body>
</html>
```